Business card design needed for rebranded top-end landscaping business

We need a new business card design, incorporating our logo (colours Green #8dc63f and Grey #8a8c8e) and also some options that include the colour dark navy (eg #000040) as our uniforms are navy with white and grey trim.

We are an innovative landscaping company that maintains high-end gardens for meticulous clients. We pride ourselves on our customer service, our professionalism, and our workmanship.

Our business name needs to be easily read and our branding needs to be bold and memorable, without screaming "tradesman"! We prefer clean lines over lots of fine detail.

The design MUST include:
- Business name ("Brambleton Gardenworks")
- Logo (file uploaded)
- Employee name
- Phone number
- Email address
- www.brambletongardenworks.com.au
- Facebook & Instagram logos
- The Turfcraft Guild logo (file uploaded) along with the word "Member"
- Licence "Lic. 618392K"

OPTIONAL inclusions:
- "Creating outdoor spaces for our community to be inspired, refreshed and re-energised"
- "Landscape Maintenance - Irrigation - Arboriculture" (dashes can be replaced with dots or other)
- "Fully qualified, licensed & insured"
- "Residential - Strata - Commercial - Real Estate" (dashes can be replaced with dots or other)

High-end professionals and retirees, real estate agents

Landscaping

See Project description

Sans Serif

Designer to choose colors to be used in the design.

• Must incorporate our logo, and colours Green #8dc63f and Grey #8a8c8e) from the logo, and the colour DARK NAVY (eg #000040).
• The design MUST include:
• - Business name ("Brambleton Gardenworks")
• - Logo (file uploaded)
• - Employee name
• - Phone number
• - Email address
• - www.brambletongardenworks.com.au
• - Facebook & Instagram logos
• - The Turfcraft Guild logo (file uploaded) along with the word "Member"
• - Licence "Lic. 618392K"
• OPTIONAL inclusions:
• - "Creating outdoor spaces for our community to be inspired, refreshed and re-energised"
• - "Landscape Maintenance - Irrigation - Arboriculture" (dashes can be replaced with dots or other)
• - "Fully qualified, licensed & insured"
• - "Residential - Strata - Commercial - Real Estate" (dashes can be replaced with dots or other)

```html
<!DOCTYPE html>
<html lang="en">
<head>
<meta charset="utf-8">
<title>Brambleton Gardenworks – Business Card</title>
<link rel="stylesheet" href="https://fonts.googleapis.com/css2?family=Montserrat:wght@500;600;700&display=swap">
<style>
  :root {
    --green: #8dc63f;
    --grey: #8a8c8e;
    --navy: #13113b;
    --board: #d1d2d4;
    --white: #ffffff;
    --ink: #3a3a3c;
  }
  * { margin: 0; padding: 0; box-sizing: border-box; }
  html, body { width: 1120px; height: 1200px; overflow: hidden; }
  body {
    position: relative;
    background: var(--board);
    font-family: "Montserrat", sans-serif;
  }
  .side-band {
    position: absolute; left: 880px; top: 0; width: 240px; height: 1200px;
    background: var(--navy);
  }
  .card {
    position: absolute; width: 549px; height: 335px;
    background: var(--white); border-radius: 22px; overflow: hidden;
    box-shadow: 4px 5px 6px rgba(0,0,0,0.35);
  }
  .card-front { left: 178px; top: 207px; }
  .card-back  { left: 177px; top: 635px; }
  .wave { position: absolute; left: 0; top: 0; width: 549px; height: 335px; }

  /* front */
  .brand-mark {
    position: absolute; left: 232px; top: 59px; width: 92px; height: 92px;
    border-radius: 50%; background: var(--grey);
  }
  .brand-name {
    position: absolute; left: 0; width: 549px; text-align: center;
    color: var(--green); font-weight: 700; line-height: 1;
  }
  .brand-name-main { top: 160px; font-size: 36px; }
  .brand-name-sub { top: 196px; font-size: 17px; letter-spacing: 1.5px; }
  .services {
    position: absolute; left: 0; top: 231px; width: 549px; text-align: center;
    color: var(--grey); font-size: 11px; font-weight: 600;
  }

  /* back */
  .guild-badge {
    position: absolute; left: 84px; top: 112px; width: 108px; height: 56px;
    border-radius: 4px; background: #e3e4e5;
  }
  .member {
    position: absolute; left: 78px; top: 176px; width: 120px;
    color: var(--green); font-size: 13px; font-weight: 700;
    letter-spacing: 10.5px; text-align: center;
  }
  .divider-v {
    position: absolute; left: 249px; top: 113px; width: 2px; height: 72px;
    background: var(--green);
  }
  .divider-h {
    position: absolute; left: 249px; top: 168px; width: 219px; height: 2px;
    background: var(--green);
  }
  .person-name, .person-role, .contact-line {
    position: absolute; right: 81px; text-align: right;
    color: var(--green); font-weight: 700; white-space: nowrap;
  }
  .person-name { top: 145px; font-size: 14px; letter-spacing: 1.6px; }
  .person-role { top: 179px; font-size: 9px; letter-spacing: 0.8px; }
  .contact-line { font-size: 7.6px; letter-spacing: 0.4px; }
  .contact-phone { top: 241px; right: 87px; }
  .contact-email { top: 258px; }
  .contact-web { top: 275px; }
  .contact-social { top: 295px; display: flex; align-items: center; gap: 6px; }
  .social-dot {
    width: 12px; height: 12px; border-radius: 50%; background: var(--green);
  }
  .licence {
    position: absolute; left: 82px; top: 297px;
    color: var(--green); font-size: 8px; font-weight: 700; letter-spacing: 0.8px;
  }
</style>
</head>
<body>
  <div class="side-band"></div>

  <section class="card card-front">
    <svg class="wave" viewBox="0 0 549 335" aria-hidden="true">
      <path d="M0 223 Q 275 404 549 231 L549 335 L0 335 Z" fill="var(--navy)"/>
    </svg>
    <div class="brand-mark"></div>
    <div class="brand-name brand-name-main">Brambleton</div>
    <div class="brand-name brand-name-sub">GARDENWORKS</div>
    <p class="services">Landscape Maintenance • Irrigation • Arboriculture</p>
  </section>

  <section class="card card-back">
    <svg class="wave" viewBox="0 0 549 335" aria-hidden="true">
      <path d="M0 0 L549 0 L549 110 Q 275 -68 0 102 Z" fill="var(--navy)"/>
    </svg>
    <div class="guild-badge"></div>
    <p class="member">MEMBER</p>
    <div class="divider-v"></div>
    <div class="divider-h"></div>
    <p class="person-name">TOMAS WHITFIELD</p>
    <p class="person-role">EMPLOYEE</p>
    <p class="contact-line contact-phone">0400-123-987</p>
    <p class="contact-line contact-email">INFO@BRAMBLETONGARDENWORKS.COM.AU</p>
    <p class="contact-line contact-web">WWW.BRAMBLETONGARDENWORKS.COM.AU</p>
    <p class="contact-line contact-social"><span class="social-dot"></span>BRAMBLETONGARDENWORKS</p>
    <p class="licence">LIC. 618392K</p>
  </section>
</body>
</html>
```